Business Card design for amazing new Dental Office

Please read this brief closely!

Our client is a modern new dental office/
They love their new logo.
Now it's time to create a business card for them.

It should be a two sided card:
Side one should have the logo and name and maybe a color background or design.
Side two should have all the contact information which is here:

Marcus Holloway, D.D.S
General and Cosmetic Dentistry
4187 W. Pinecrest Avenue
Ventura, CA 93011
(805) 912-4386
drmarcus@bluefernsmiles-example.com
www.bluefernsmiles-example.com

Feel free to arrange that info as you like and to style both sides of the card according to your creativity. This is a chance for you to show your design skills!

Client is open to font choices and is looking for a style that is amazing and premium. Colors can be selected from the logo, or any variation of those.

You will not win this contest with a less than beautiful card design so please feel free to make multiple submissions.

Logo files attached and please message me with any questions.
Thanks!

Target Market(s)

Families and Professionals seeking dental services

Industry/Entity Type

Dental

Contact Information for Business Card

Logo, style, contact info as per the brief

Font styles to use
Sans Serif

Requirements
Must have
• Client's logo and contact details as per brief
Nice to have
• Unique style reflecting high end dental clinic near the beach
Should not have
• Must not look like a template

```html
<!DOCTYPE html>
<html lang="en">
<head>
<meta charset="utf-8">
<title>Blue Fern Smiles – Business Card</title>
<link rel="stylesheet" href="https://fonts.googleapis.com/css2?family=Poppins:wght@300;400;800&display=swap">
<style>
  :root {
    --stage: #1c1d1f;
    --sky: #4bb1e4;
    --sand: #e0a861;
    --sea: #69c1bb;
    --paper: #ffffff;
    --ink: #2b2b2b;
    --mist: #a7a9ac;
  }
  * { box-sizing: border-box; margin: 0; padding: 0; }
  html, body {
    width: 1200px; height: 912px; overflow: hidden;
    background: var(--stage);
    font-family: "Poppins", sans-serif;
  }
  .card {
    position: absolute;
    width: 620px; height: 354px;
    border-radius: 16px;
    overflow: hidden;
  }
  .card--front {
    left: 60px; top: 60px;
    background: var(--sky);
  }
  .card--back {
    left: 520px; top: 498px;
    background: var(--paper);
  }
  .front-pattern {
    position: absolute; inset: 0;
    background: linear-gradient(160deg, #4bb1e4 0%, #43a8da 55%, #4bb1e4 100%);
  }
  .front-name {
    position: absolute; left: 0; right: 0; top: 155px;
    text-align: center;
    color: var(--paper);
    font-weight: 300;
    font-size: 34px;
    letter-spacing: 5px;
  }
  .back-waves { position: absolute; inset: 0; }
  .back-title {
    position: absolute; right: 30px; top: 28px;
    text-align: right;
  }
  .back-title__name {
    color: var(--sand);
    font-weight: 800;
    font-size: 20px;
    letter-spacing: 0.3px;
    text-transform: uppercase;
  }
  .back-title__role {
    color: var(--paper);
    font-weight: 400;
    font-size: 13px;
  }
  .back-brand {
    position: absolute; right: 30px; top: 228px;
    color: var(--mist);
    font-weight: 300;
    font-size: 20px;
    letter-spacing: 2px;
  }
  .contact {
    position: absolute; left: 36px; top: 236px;
    color: var(--ink);
    font-size: 12.5px;
    line-height: 17px;
    list-style: none;
  }
  .contact__line { display: flex; align-items: center; gap: 7px; }
  .contact__address { margin-bottom: 2px; }
  .contact__icon { width: 11px; height: 11px; flex: none; }
</style>
</head>
<body>
  <section class="card card--front">
    <div class="front-pattern" role="img" aria-label="Soft blue wave pattern background"></div>
    <div class="front-name">BLUE FERN SMILES</div>
  </section>

  <section class="card card--back">
    <svg class="back-waves" viewBox="0 0 620 354" width="620" height="354" aria-hidden="true">
      <path fill="var(--sea)"   d="M0 0H620V82C585 142 505 174 405 194C270 218 75 226 0 230Z"/>
      <path fill="var(--paper)" d="M0 0H620V76C587 137 510 166 410 185C274 208 77 214 0 217Z"/>
      <path fill="var(--sand)"  d="M0 0H620V71C588 133 513 162 413 181C276 204 78 209 0 211Z"/>
      <path fill="var(--paper)" d="M0 0H620V64C589 126 517 154 417 173C278 196 79 200 0 201Z"/>
      <path fill="var(--sky)"   d="M0 0H620V58C590 120 520 148 420 167C280 190 80 194 0 192Z"/>
    </svg>

    <header class="back-title">
      <div class="back-title__name">Marcus Holloway, D.D.S</div>
      <div class="back-title__role">General and Cosmetic Dentistry</div>
    </header>

    <div class="back-brand">BLUE FERN SMILES</div>

    <ul class="contact">
      <li class="contact__address">4187 W. Pinecrest Avenue<br>Ventura, CA 93011</li>
      <li class="contact__line">
        <svg class="contact__icon" viewBox="0 0 12 12" aria-hidden="true"><path fill="var(--sky)" d="M2.5 1l2 2.3-1.2 1.3a7 7 0 0 0 4.1 4.1l1.3-1.2 2.3 2-1.3 1.6C5.2 11 1 6.8.9 2.3z"/></svg>
        (805) 912-4386
      </li>
      <li class="contact__line">
        <svg class="contact__icon" viewBox="0 0 12 12" aria-hidden="true"><rect x="0.5" y="2" width="11" height="8" rx="1" fill="var(--sky)"/><path d="M1 2.8l5 3.6 5-3.6" stroke="#fff" stroke-width="1" fill="none"/></svg>
        drmarcus@bluefernsmiles-example.com
      </li>
      <li class="contact__line">
        <svg class="contact__icon" viewBox="0 0 12 12" aria-hidden="true"><circle cx="6" cy="6" r="5.3" fill="var(--sky)"/><path d="M.8 6h10.4M6 .7c-2.6 3-2.6 7.6 0 10.6M6 .7c2.6 3 2.6 7.6 0 10.6" stroke="#fff" stroke-width=".8" fill="none"/></svg>
        www.bluefernsmiles-example.com
      </li>
    </ul>
  </section>
</body>
</html>
```